Front cover of trifold brochure

This is for my real estate company. I need a design for the front page of the tri fold brochure. The interior of the brochure will constantly change, however I wanted to update the front cover to something more modern. I sell high end vacation homes on a Grand Lake, located in Northeast Oklahoma. So something that would appeal to vacation/second lake home buyers would be great. My logo colors are orange and burgundy, if we could incorporate those colors that would be great. I have attached a zip drive with all of the versions of my logo. I want to have a logo on there, as well as my phone number and my website. My website is www.tresslowandco.com, and my office number is 555-310-4826.

```html
<!DOCTYPE html>
<html lang="en">
<head>
<meta charset="utf-8">
<title>Tresslow &amp; Company Realty – Trifold Brochure Outside</title>
<link rel="stylesheet" href="https://fonts.googleapis.com/css2?family=Montserrat:wght@400;500;600;700;800&display=swap">
<style>
  :root {
    --backdrop: #d9d9d9;
    --orange: #c9722f;
    --orange-deep: #b9622a;
    --burgundy: #6a1a26;
    --burgundy-dark: #4a0f19;
    --ink-brown: #4a1a0e;
    --white: #ffffff;
    --sky-top: #2f6fc4;
    --sky-low: #9cc4e8;
    --lawn: #5f9a3a;
    --stone: #b9946a;
  }
  * { margin: 0; padding: 0; box-sizing: border-box; }
  html, body { width: 898px; height: 1200px; overflow: hidden; }
  body {
    background: var(--backdrop);
    font-family: "Montserrat", Arial, sans-serif;
    color: var(--white);
  }
  .brochure {
    position: absolute;
    left: 19px; top: 268px;
    width: 860px; height: 664px;
    overflow: hidden;
    box-shadow: 0 6px 18px rgba(0,0,0,0.25);
  }
  .brochure-art { position: absolute; inset: 0; }

  /* About panel */
  .about-panel {
    position: absolute; left: 28px; top: 110px; width: 220px;
  }
  .about-title { font-size: 15px; font-weight: 700; letter-spacing: 1px; }
  .about-subtitle { font-size: 9px; font-weight: 600; margin: 4px 0 10px; }
  .about-body { font-size: 7.5px; line-height: 1.55; margin-bottom: 8px; opacity: 0.92; }

  /* Brand name lockups */
  .brand { display: flex; align-items: center; gap: 7px; font-weight: 600; color: var(--white); }
  .brand-mark { width: 14px; height: 14px; background: var(--white); flex: none; }
  .brand-name { line-height: 1.1; }
  .brand--back { position: absolute; left: 300px; top: 438px; font-size: 13px; }
  .brand--cover { position: absolute; left: 690px; top: 70px; font-size: 15px; }

  /* Contact block on the back panel */
  .contact {
    position: absolute; left: 300px; top: 560px; width: 250px;
    text-align: center; font-size: 9.5px; font-weight: 500;
  }
  .contact-line { display: flex; flex-direction: column; align-items: center; margin-bottom: 5px; }
  .contact-line svg { width: 11px; height: 11px; margin-bottom: 2px; }

  /* Cover headline */
  .cover-headline {
    position: absolute; left: 626px; top: 418px;
    transform: rotate(21deg); transform-origin: left top;
    width: 260px;
  }
  .headline-high { font-size: 17px; font-weight: 800; color: var(--ink-brown); line-height: 1; }
  .headline-vacation { font-size: 17px; font-weight: 800; color: var(--white); line-height: 1.1; }
  .headline-sale { font-size: 40px; font-weight: 800; color: var(--ink-brown); line-height: 1; letter-spacing: 1px; }
  .headline-location { font-size: 10.5px; font-weight: 500; margin-top: 4px; line-height: 1.3; }
  .headline-web { font-size: 9px; font-weight: 500; margin-top: 18px; margin-left: 14px; }
</style>
</head>
<body>
  <main class="brochure">
    <svg class="brochure-art" width="860" height="664" viewBox="0 0 860 664">
      <defs>
        <linearGradient id="aboutPhotoTint" x1="0" y1="0" x2="0" y2="1">
          <stop offset="0" stop-color="#7a2230"/>
          <stop offset="0.6" stop-color="#5a1420"/>
          <stop offset="1" stop-color="#a23a2a"/>
        </linearGradient>
        <linearGradient id="resortPhoto" x1="0" y1="0" x2="0" y2="1">
          <stop offset="0" stop-color="#2f6fc4"/>
          <stop offset="0.35" stop-color="#9cc4e8"/>
          <stop offset="0.55" stop-color="#b9946a"/>
          <stop offset="0.8" stop-color="#8a6a4a"/>
          <stop offset="1" stop-color="#5f9a3a"/>
        </linearGradient>
      </defs>
      <rect class="orange-field" width="860" height="664" fill="#c9722f"/>
      <polygon class="about-photo" points="0,0 270,0 445,485 0,560" fill="url(#aboutPhotoTint)"
               role="img" aria-label="Burgundy-tinted photo of bare trees at sunset by the lake"/>
      <polygon class="resort-photo" points="270,0 860,0 860,505 608,392 445,485" fill="url(#resortPhoto)"
               role="img" aria-label="Photo of a stone and timber lakeside resort lodge under a blue sky with a green lawn"/>
      <polyline points="270,0 445,485 608,392 860,505" fill="none" stroke="#ffffff" stroke-width="5" stroke-opacity="0.85"/>
      <polyline points="0,560 445,485" fill="none" stroke="#b9622a" stroke-width="2"/>
      <line x1="287" y1="0" x2="287" y2="664" stroke="#000" stroke-opacity="0.08"/>
      <line x1="573" y1="0" x2="573" y2="664" stroke="#000" stroke-opacity="0.08"/>
    </svg>

    <section class="about-panel">
      <h2 class="about-title">ABOUT</h2>
      <p class="about-subtitle">The Grand Lake Experience</p>
      <p class="about-body">You share the wonder of Grand Lake with family and friends every season. Our team knows the shoreline, the coves and the quiet roads, and we guide you toward a home that fits the way you want to spend your days.</p>
      <p class="about-body">From weekend cabins to grand lakefront estates, we handle every detail with care. Call us today and let us show you why buyers return to the Grand Lake experience year after year.</p>
    </section>

    <div class="brand brand--back">
      <span class="brand-mark"></span>
      <span class="brand-name">Tresslow<br>&amp; Company Realty</span>
    </div>

    <section class="contact">
      <div class="contact-line">
        <svg viewBox="0 0 24 24"><path fill="#fff" d="M6.6 10.8a15 15 0 0 0 6.6 6.6l2.2-2.2c.3-.3.7-.4 1-.2 1.1.4 2.3.6 3.6.6.6 0 1 .4 1 1V20c0 .6-.4 1-1 1A17 17 0 0 1 3 4c0-.6.4-1 1-1h3.5c.6 0 1 .4 1 1 0 1.3.2 2.5.6 3.6.1.3 0 .7-.2 1z"/></svg>
        <span>555.310.4826</span>
      </div>
      <div class="contact-line">
        <svg viewBox="0 0 24 24"><rect x="2" y="5" width="20" height="14" rx="2" fill="#fff"/><path d="M3 6l9 7 9-7" fill="none" stroke="#c9722f" stroke-width="2"/></svg>
        <span>jordan@tresslowandco.net</span>
      </div>
      <div class="contact-line">
        <svg viewBox="0 0 24 24"><circle cx="12" cy="12" r="10" fill="#fff"/><path d="M2 12h20M12 2c3 3 3 17 0 20M12 2c-3 3-3 17 0 20" fill="none" stroke="#c9722f" stroke-width="1.5"/></svg>
        <span>www.tresslowandco.com</span>
      </div>
    </section>

    <div class="brand brand--cover">
      <span class="brand-mark"></span>
      <span class="brand-name">Tresslow<br>&amp; Company Realty</span>
    </div>

    <section class="cover-headline">
      <p class="headline-high">HIGH END</p>
      <p class="headline-vacation">VACATION HOMES</p>
      <h1 class="headline-sale">ON SALE</h1>
      <p class="headline-location">Located in Grand lake, Northeast<br>Oklahoma</p>
      <p class="headline-web">www.tresslowandco.com</p>
    </section>
  </main>
</body>
</html>
```